Business card website / business card for website

We are a French website selling products Made in USA of quality, we need a business card to give from hand to hand and for deposit in the cartons of Each order. We-have the logo That I send in the attachments The theme is: US Vintage and find the compromised entre les national park ambience us and the atmosphere Brooklyn If you can make the feeling it's great The site www.latablederivebleue.com (opening April) You can change the logo a little gold in color it could ... we are a French website selling products Made in USA quality, we need a business card to give from hand to hand and deposit in cartons each order. we have the logo that I convey in the attached parts is the theme: Vintage embiance US and find a compromise between the atmosphere us national park and the atmosphere Brooklyn at: www.latablederivebleue.com (opening April) if you can the impression is great

Target Market(s)

25-50 YEARS man, woman.

Industry/Entity Type

Business

Contact Information for Business Card

www.latablederivebleue.com
N'oubliez pas que nous sommes là si vous avez besoin de nouscontact@latablederivebleue.com

Font styles to use
Serif

Requirements
Must have
• my logo with "general store", my email address preceded by the phrase: Do not forget that we are here if you need us My logo with the words "general store," my email address Preceded by the sentence: remember we're here if you need us (in french)
Nice to have
• i like this style: http://designcorbel.net/ideas/print-ideas/25-charming-old-style-business-card-designs/ must feel the Vintage America it must feel the Vintage America lice can change a little logo or to color ... You can change the logo a little gold in color it could ... i like kraft paper with red ....
Should not have

```html
<!DOCTYPE html>
<html lang="fr">
<head>
<meta charset="utf-8">
<title>La Table de Rive Bleue — Carte de visite</title>
<link href="https://fonts.googleapis.com/css2?family=Open+Sans:wght@400;600&display=swap" rel="stylesheet">
<style>
  :root {
    --backdrop: #2b2b2b;
    --kraft: #ebe2ca;
    --kraft-edge: #d9ceb1;
    --ink: #1f1d1b;
    --red: #a8322d;
    --rule: #3a3633;
  }
  html, body {
    margin: 0;
    width: 1200px;
    height: 1000px;
    overflow: hidden;
    background: var(--backdrop);
  }
  .canvas {
    position: relative;
    width: 1200px;
    height: 1000px;
    display: flex;
    align-items: center;
    justify-content: center;
  }
  .card {
    position: relative;
    width: 520px;
    height: 880px;
    box-sizing: border-box;
    padding: 50px 56px;
    background: radial-gradient(circle at 40% 30%, #efe7d1 0%, var(--kraft) 55%, var(--kraft-edge) 100%);
    box-shadow: 0 12px 30px rgba(0,0,0,.5);
    font-family: "Open Sans", Arial, sans-serif;
    color: var(--ink);
  }
  .brand {
    display: flex;
    flex-direction: column;
    align-items: center;
    gap: 22px;
    margin-top: 10px;
  }
  .brand-circle {
    width: 250px;
    height: 250px;
    border: 2px solid var(--ink);
    border-radius: 50%;
  }
  .brand-name {
    font-size: 22px;
    font-weight: 600;
    letter-spacing: 2px;
    color: var(--ink);
    text-transform: uppercase;
  }
  .store-label {
    text-align: center;
    font-size: 34px;
    letter-spacing: 2px;
    margin: 34px 0 24px;
  }
  .rule {
    border: none;
    border-top: 3px dotted var(--rule);
    margin: 0 -20px;
  }
  .person {
    padding: 28px 0 26px;
  }
  .person-name {
    font-size: 28px;
    letter-spacing: 1px;
    margin: 0;
  }
  .person-name .surname { color: var(--red); }
  .person-role {
    font-size: 20px;
    color: var(--red);
    margin: 2px 0 0;
  }
  .contacts {
    list-style: none;
    margin: 24px 0 0;
    padding: 0;
    font-size: 20px;
  }
  .contacts li {
    display: flex;
    align-items: center;
    gap: 16px;
    margin-bottom: 12px;
  }
  .contacts svg { width: 22px; height: 22px; flex: none; }
  .reminder {
    font-size: 20px;
    line-height: 1.35;
    margin: 14px 0 14px;
  }
</style>
</head>
<body>
<main class="canvas">
  <article class="card">
    <header class="brand">
      <div class="brand-circle"></div>
      <div class="brand-name">La Table de Rive Bleue</div>
    </header>

    <p class="store-label">GÉNÉRAL STORE</p>
    <hr class="rule">

    <section class="person">
      <p class="person-name">LUCIEN <span class="surname">MARCHAL</span></p>
      <p class="person-role">FONDATEUR &amp; CEO</p>
    </section>

    <hr class="rule">

    <ul class="contacts">
      <li>
        <svg viewBox="0 0 24 24" aria-hidden="true"><path fill="#a8322d" d="M6.6 10.8a15.1 15.1 0 0 0 6.6 6.6l2.2-2.2c.3-.3.7-.4 1-.2 1.1.4 2.3.6 3.6.6.6 0 1 .4 1 1V20c0 .6-.4 1-1 1A17 17 0 0 1 3 4c0-.6.4-1 1-1h3.5c.6 0 1 .4 1 1 0 1.3.2 2.5.6 3.6.1.3 0 .7-.2 1z"/></svg>
        <span>+000 321 654 987</span>
      </li>
      <li>
        <svg viewBox="0 0 24 24" aria-hidden="true"><circle cx="12" cy="12" r="10" fill="none" stroke="#a8322d" stroke-width="2"/><path d="M2 12h20M12 2c3 3 3 17 0 20M12 2c-3 3-3 17 0 20" fill="none" stroke="#a8322d" stroke-width="1.6"/></svg>
        <span>www.latablederivebleue.com</span>
      </li>
    </ul>

    <p class="reminder">N'oubliez pas que nous sommes<br>ici si vous avez besoin de nous</p>

    <ul class="contacts">
      <li>
        <svg viewBox="0 0 24 24" aria-hidden="true"><rect x="2" y="5" width="20" height="14" fill="#a8322d"/><path d="M2 5l10 8 10-8" fill="none" stroke="#ebe2ca" stroke-width="1.6"/></svg>
        <span>contact@latablederivebleue.com</span>
      </li>
    </ul>
  </article>
</main>
</body>
</html>
```